Corevia health fitness personal training classes 8 week challenges

Corevia (aust) pty ltd is the business name I have only a Facebook page corevia Marlene

I instruct 4 classes fitness classes a week and run 8 week challenges aprox 3-5 a year. I do personal training and write programs
These web sites are similar to what Iam looking for
Tara holt 8 week program
Laura Pine
Harriet coombs

The above sites offer what I offer
Bonus is mine can be done online and in person which can be draining since I then take in a lot of emotional stuff and stories and excuses from clients

They get given training programs which is what I do written programs but I also give them physical training sessions as well

The purpose of this site?
My goal is to stay in the health and fitness industry however my body is physically, emotionally mentally exhausted.
I am torn because I love my job but 28 years later and with a few health issues I can't do it.
I must stop i need to stop due to
My health but I can't I worry about the loss of income and letting people down

So if I can set up a website and a online app, 8 week challenge or add to my collection of fitness DVDs and put them online where I can work from home

on my Facebook you can access my albums and advertising material

My main primary audience is females between 25-55 however I cater for everyone young old for unfit challenged etc

On my website or app these are the things I would want to cover

Everyday there would be a new inspirational logo
A short program they can do in the privacy of there home
My fitness DVD's and workout clothing on sale
Fitness programs on sale

I have an in in inbundance of information I can draw from of eg my 3 fitness DVDs, receipes, logos, inspirational quotes from my Facebook so stuff I have used before I am wanting to produce another DVD And complete my book I would love to add that to my products

Eye catching words
Weight loss (only because that gets people in straight away)
Fat burner (example I teach a abs thigh butt class Monday yes it's burns calories as much as the Fatburner class but uneducated people will go to the Fatburner just because of the name

Corevia

28 years experience ( I believe i have so much experience and stories to share I have the qualifications and awards that I have won but it's my passion and desire to help others I think this is why my business is a success.
Can this translate online ??

I have won fitness professional awards

I want people to connect with me and I want there first reaction to be of hope and courage and know that they can do this that real wow anything is possible
Corevia is about the member and I genuinely care Yhey are not just a number

​I want them to trust that I have the knowledge and experience
Online fitness programs
The selling of my fitness DVDs
Online 8 week programs
Recipes
Before and after photos
Client testimonials

Target Market(s)

Majority a females aged between 18-60 years old

Industry/Entity Type

Health And Wellness

Coding

Coded - Design and coding required

Number of Pages Required

1 page

Font styles to use
Serif
Script

Colors
f37122
faa54b
3c7bb8
33a6d7

Requirements
Must have
• Albums / files as below
• Client testimonials
• Before and after photos
• Selling products eg DVD's/ programs etc
Nice to have
• My aim is to take my business more into online so I can still offer all my services eg classes, programs, nutritional advice, one on one consultant,
• However have the bonus of doing it from home online.
• Also my body needs to physically slow down
Should not have
• Not sure on this question

```html
<!DOCTYPE html>
<html lang="en">
<head>
<meta charset="utf-8">
<title>Corevia – Mind &amp; Body Fitness</title>
<link rel="stylesheet" href="https://fonts.googleapis.com/css2?family=Lato:ital,wght@0,400;0,700;0,900;1,700;1,900&display=swap">
<style>
:root{
  --orange:#f37122;
  --orange-soft:#faa54b;
  --blue:#3c7bb8;
  --ink:#2c2c2c;
  --dark:#262626;
  --darker:#1c1c1c;
  --grey:#8a8a8a;
  --light:#e3e3e3;
  --text:#666;
  --white:#fff;
}
*{box-sizing:border-box;margin:0;padding:0}
html,body{width:1200px;height:3920px;overflow:hidden}
body{font-family:"Lato",Arial,sans-serif;color:var(--text);background:var(--white);position:relative}
.abs{position:absolute}
.photo{position:absolute}

/* header */
.site-header{position:absolute;top:0;left:0;width:1200px;height:72px;background:var(--white);display:flex;align-items:center;justify-content:space-between;padding:0 64px;box-shadow:0 1px 4px rgba(0,0,0,.08);z-index:2}
.brand{display:flex;align-items:center;gap:8px;font-weight:900;font-size:22px;letter-spacing:1px;color:var(--orange)}
.brand-mark{width:14px;height:14px;background:var(--orange)}
.main-nav{display:flex;align-items:center;gap:30px;font-size:15px;color:#555}
.main-nav .active{color:var(--orange);border-bottom:2px solid var(--orange);padding-bottom:4px}
.login-btn{background:var(--orange);color:var(--white);padding:8px 18px;font-size:14px}

/* hero */
.hero{position:absolute;top:72px;left:0;width:1200px;height:468px;background:linear-gradient(115deg,#3d4752 0%,#6f7780 45%,#a9aeb2 75%,#7a8088 100%)}
.hero-shade{position:absolute;inset:0;background:linear-gradient(90deg,rgba(20,20,20,.55),rgba(20,20,20,0) 60%)}
.hero-copy{position:absolute;left:64px;top:100px;color:var(--white)}
.hero-title{font-weight:900;font-style:italic;font-size:66px;line-height:70px;text-transform:uppercase}
.hero-title .accent{color:var(--orange)}
.hero-sub{font-size:22px;font-weight:700;letter-spacing:1px;margin-top:14px}
.hero-btn{display:inline-block;margin-top:36px;background:var(--ink);color:var(--white);font-size:15px;font-weight:700;padding:10px 20px}
.hero-dots{position:absolute;right:64px;bottom:60px;display:flex;gap:8px}
.hero-dots span{width:8px;height:8px;border-radius:50%;background:rgba(255,255,255,.5)}
.hero-dots span:first-child{background:var(--white)}

/* headings */
.section-title{position:absolute;left:0;width:1200px;text-align:center;font-weight:900;font-style:italic;font-size:26px;text-transform:uppercase;color:var(--ink)}
.section-title .accent{color:var(--orange)}
.title-rule{position:absolute;left:0;width:1200px;display:flex;justify-content:center;align-items:center;gap:8px}
.title-rule i{width:80px;height:1px;background:#bbb;display:block}
.title-rule b{width:10px;height:10px;border:1px solid #bbb;transform:rotate(45deg);display:block}

/* challenges */
.challenge{position:absolute;top:712px;width:316px;height:316px;display:flex;align-items:center;justify-content:center}
.challenge-label{border:2px solid rgba(255,255,255,.8);color:var(--white);font-size:26px;padding:10px 18px;background:rgba(0,0,0,.25)}

/* intro */
.intro{position:absolute;top:1120px;left:0;width:1200px;height:480px;background:var(--dark)}
.intro-copy{position:absolute;left:64px;top:80px;width:400px;color:#bbb;font-size:13px;line-height:20px}
.intro-title{font-weight:900;font-style:italic;font-size:28px;color:var(--white);text-transform:uppercase;margin-bottom:18px}
.intro-title .accent{color:var(--orange)}
.intro-copy p{margin-bottom:16px}
.intro-copy .lead{color:#ddd}
.intro-copy .lead b{color:var(--orange)}
.outline-btn{display:inline-block;border:1px solid #bbb;color:var(--white);font-size:13px;font-weight:700;padding:8px 16px;margin-top:14px}
.intro-photo{left:490px;top:1100px;width:660px;height:540px;background:linear-gradient(135deg,#d5d2cf,#a79e98 50%,#6d6b6d);clip-path:polygon(90px 0,660px 0,660px 540px,0 540px);box-shadow:0 8px 20px rgba(0,0,0,.3)}

/* timetable */
.center-text{position:absolute;left:200px;width:800px;text-align:center;font-size:13px;line-height:22px;color:var(--text)}
.timetable{position:absolute;top:1832px;left:80px;width:1040px;height:188px;display:flex;box-shadow:0 4px 14px rgba(0,0,0,.15)}
.tt-lead{width:260px;background:var(--orange);color:var(--white);padding:40px 30px;border-left:14px solid var(--ink)}
.tt-lead h3{font-size:44px;font-weight:400;line-height:46px}
.tt-lead p{font-size:22px}
.tt-pager{display:flex;gap:4px;margin-top:18px}
.tt-pager span{width:18px;height:18px;background:var(--white);opacity:.7}
.tt-pager span:last-child{background:var(--blue);opacity:1}
.tt-day{width:260px;padding:26px 24px;font-size:13px}
.tt-day h4{font-size:15px;font-weight:700;color:var(--ink)}
.tt-time{margin:6px 0 14px;padding-bottom:14px;border-bottom:1px solid rgba(0,0,0,.15);display:flex;align-items:center;gap:6px}
.tt-class{font-size:21px;color:var(--orange);text-transform:uppercase;margin-bottom:8px;white-space:nowrap}
.tt-day.mon{background:var(--white)}
.tt-day.tue{background:var(--light)}
.tt-day.wed{background:var(--grey);color:var(--white)}
.tt-day.wed h4,.tt-day.wed .tt-class{color:var(--white)}

/* before after */
.results{position:absolute;top:2160px;left:0;width:1200px;height:440px;background:var(--darker)}
.result-photo{position:absolute;top:30px;width:520px;height:380px;background:linear-gradient(180deg,#f1e7df 0%,#e4cfc2 55%,#3b3b3b 56%,#2e2e2e 100%)}
.result-tag{position:absolute;top:42px;background:var(--orange);color:var(--white);font-size:12px;font-weight:900;padding:4px 12px}
.result-split{position:absolute;left:599px;top:30px;width:2px;height:380px;background:var(--orange)}
.result-knob{position:absolute;left:584px;top:204px;width:32px;height:32px;border-radius:50%;background:var(--orange);border:3px solid var(--white)}

/* blog */
.blog-card{position:absolute;top:2740px;width:336px;height:320px;background:var(--white);box-shadow:0 4px 14px rgba(0,0,0,.15)}
.blog-img{height:250px}
.blog-date{position:absolute;left:14px;top:236px;background:var(--orange);color:var(--white);font-size:11px;padding:4px 10px}
.blog-body{padding:16px 18px;font-size:13px;line-height:18px}
.blog-body h4{font-size:14px;color:var(--ink);font-weight:400}
.blog-corner{position:absolute;right:0;bottom:0;width:0;height:0;border-left:28px solid transparent;border-bottom:28px solid var(--orange)}

/* testimonial + footer */
.testimonial{position:absolute;top:3200px;left:0;width:1200px;height:280px;background:linear-gradient(180deg,#2b2b2b,#222)}
.quote-mark{position:absolute;left:96px;top:60px;font-size:60px;font-weight:900;color:var(--orange);line-height:40px}
.quote-text{position:absolute;left:96px;top:110px;width:1010px;color:var(--white);font-size:16px;line-height:26px}
.quote-name{position:absolute;left:96px;top:214px;color:var(--white);font-size:12px;font-weight:700}
.quote-dots{position:absolute;left:96px;top:246px;display:flex;gap:6px}
.quote-dots span{width:8px;height:8px;background:#666}
.quote-dots span:first-child{background:var(--orange)}
.site-footer{position:absolute;top:3480px;left:0;width:1200px;height:400px;background:var(--darker);color:#aaa;font-size:13px}
.footer-brand{position:absolute;left:64px;top:140px;background:var(--white);padding:14px 18px}
.footer-col{position:absolute;top:140px}
.footer-col h5{color:var(--white);font-size:15px;font-weight:700;margin-bottom:16px}
.footer-col li{list-style:none;margin-bottom:10px;display:flex;align-items:center;gap:8px}
.footer-col li::before{content:"";width:5px;height:5px;background:var(--orange)}
.footer-col.contact li::before{display:none}
.news{display:flex;margin-top:4px}
.news span{width:190px;height:30px;background:#333;color:#777;font-size:12px;padding:7px 10px}
.news b{width:30px;height:30px;background:var(--orange)}
.follow{display:flex;align-items:center;gap:8px;margin-top:14px}
.follow i{width:16px;height:16px;border-radius:50%;background:var(--orange);display:block}
.copyright{position:absolute;top:3880px;left:0;width:1200px;height:40px;background:#111;color:#999;font-size:12px;text-align:center;line-height:40px}
</style>
</head>
<body>

<header class="site-header">
  <div class="brand"><span class="brand-mark"></span>COREVIA</div>
  <nav class="main-nav">
    <span class="active">Home</span><span>About Us</span><span>Testimonial</span><span>Products</span><span>Blogs</span><span>Contact Us</span>
    <span class="login-btn">Login</span>
  </nav>
</header>

<section class="hero" role="img" aria-label="Trainer coaching a woman through a workout in a gym">
  <div class="hero-shade"></div>
  <div class="hero-copy">
    <h1 class="hero-title"><span class="accent">Mind</span> &amp; Body<br>Fitness</h1>
    <p class="hero-sub">RESULTS GUARANTEED</p>
    <span class="hero-btn">GET STARTED NOW</span>
  </div>
  <div class="hero-dots"><span></span><span></span><span></span></div>
</section>

<h2 class="section-title" style="top:622px">Try one of our <span class="accent">challenges</span></h2>
<div class="title-rule" style="top:668px"><i></i><b></b><i></i></div>

<div class="challenge" style="left:64px;background:linear-gradient(135deg,#c9b6a6,#7e6a60)" role="img" aria-label="Woman exercising for weight loss"><span class="challenge-label">Weight Loss</span></div>
<div class="challenge" style="left:442px;background:linear-gradient(135deg,#b79a8a,#5e4c48)" role="img" aria-label="Woman in a fat burner workout"><span class="challenge-label">Fat Burner</span></div>
<div class="challenge" style="left:820px;background:linear-gradient(135deg,#a07a72,#4e3a3c)" role="img" aria-label="Group class for all fitness levels"><span class="challenge-label">All Level</span></div>

<section class="intro">
  <div class="intro-copy">
    <h2 class="intro-title">Introducing <span class="accent">Corevia</span></h2>
    <p class="lead"><b>Corevia</b> challenge 8 Weeks or add to my collection of fitness DVDs.</p>
    <p>Ut enim ad minim veniam, quis nostrud exercitation ullamco laboris nisi ut aliquip ex ea commodo consequat.</p>
    <p>Consectetur adipiscing elit sed do eiusmod tempor incididunt ut labore et dolore magna aliqua. Ut enim ad minim veniam quis nostrud exercitation ullamco laboris nisi ut aliquip commodo consequat.</p>
    <span class="outline-btn">READ MORE</span>
  </div>
</section>
<div class="photo intro-photo" role="img" aria-label="Trainer assisting a smiling woman on a gym bench"></div>
<svg class="abs" style="left:0;top:1560px" width="1200" height="90" viewBox="0 0 1200 90" aria-hidden="true">
  <polygon points="0,20 480,20 420,90 0,90" fill="var(--orange)"/>
  <polygon points="0,40 380,40 330,90 0,90" fill="var(--white)"/>
</svg>

<h2 class="section-title" style="top:1672px">Time table <span class="accent">of classes</span></h2>
<div class="title-rule" style="top:1716px"><i></i><b></b><i></i></div>
<p class="center-text" style="top:1736px">Lorem ipsum dolor sit amet, consectetur adipiscing elit, sed do eiusmod tempor incididunt ut labore et dolore magna aliqua. Ut enim ad minim veniam, quis nostrud exercitation ullamco laboris nisi ut aliquip ex ea.</p>

<div class="timetable">
  <div class="tt-lead">
    <h3>8 Weeks</h3><p>Classes</p>
    <div class="tt-pager"><span></span><span></span></div>
  </div>
  <div class="tt-day mon">
    <h4>Monday</h4>
    <div class="tt-time"><svg width="12" height="12" viewBox="0 0 12 12"><circle cx="6" cy="6" r="5" fill="none" stroke="currentColor"/><path d="M6 3v3h2" fill="none" stroke="currentColor"/></svg>6:00 AM - 10:00 AM</div>
    <div class="tt-class">Abs/ Thigh/ Butt</div>
    <div>Trainer: Marlene Ashby</div>
  </div>
  <div class="tt-day tue">
    <h4>Tuesday</h4>
    <div class="tt-time"><svg width="12" height="12" viewBox="0 0 12 12"><circle cx="6" cy="6" r="5" fill="none" stroke="currentColor"/><path d="M6 3v3h2" fill="none" stroke="currentColor"/></svg>6:00 AM - 10:00 AM</div>
    <div class="tt-class">Abs/ Thigh/ Butt</div>
    <div>Trainer: Marlene Ashby</div>
  </div>
  <div class="tt-day wed">
    <h4>Wednesday</h4>
    <div class="tt-time"><svg width="12" height="12" viewBox="0 0 12 12"><circle cx="6" cy="6" r="5" fill="none" stroke="currentColor"/><path d="M6 3v3h2" fill="none" stroke="currentColor"/></svg>6:00 PM - 7:00 PM</div>
    <div class="tt-class">Core Fatburner</div>
    <div>Trainer: Marlene Ashby</div>
  </div>
</div>

<svg class="abs" style="left:0;top:2080px" width="1200" height="80" viewBox="0 0 1200 80" aria-hidden="true">
  <polygon points="1200,0 1200,80 0,80 0,78" fill="var(--darker)"/>
  <polygon points="1200,0 1200,30 700,70" fill="var(--orange)"/>
</svg>

<section class="results">
  <div class="result-photo" style="left:64px" role="img" aria-label="Waist and stomach before the program"></div>
  <div class="result-photo" style="left:616px;background:linear-gradient(180deg,#f3e9e1 0%,#e8d3c6 55%,#3b3b3b 56%,#2e2e2e 100%)" role="img" aria-label="Waist and stomach after the program"></div>
  <span class="result-tag" style="left:64px">BEFORE</span>
  <span class="result-tag" style="left:1068px">AFTER</span>
  <div class="result-split"></div>
  <div class="result-knob"></div>
</section>
<svg class="abs" style="left:0;top:2600px" width="1200" height="40" viewBox="0 0 1200 40" aria-hidden="true">
  <polygon points="0,0 520,0 0,36" fill="var(--orange)"/>
</svg>

<h2 class="section-title" style="top:2652px">Our <span class="accent">latest blog</span></h2>
<div class="title-rule" style="top:2696px"><i></i><b></b><i></i></div>

<article class="blog-card" style="left:64px">
  <div class="blog-img" style="background:linear-gradient(135deg,#dfe4e8,#9fb1bf)" role="img" aria-label="Woman stretching outdoors"></div>
  <span class="blog-date">14 - 03 - 2017</span>
  <div class="blog-body"><h4>Lorem ipsum dolor sit amet</h4><p>Adipiscing elit sed do eiu</p></div>
  <span class="blog-corner"></span>
</article>
<article class="blog-card" style="left:432px">
  <div class="blog-img" style="background:linear-gradient(135deg,#d8cfc8,#6b605c)" role="img" aria-label="Group doing floor exercises in class"></div>
  <span class="blog-date">14 - 03 - 2017</span>
  <div class="blog-body"><h4>Lorem ipsum dolor sit amet</h4><p>Adipiscing elit sed do eiu</p></div>
  <span class="blog-corner"></span>
</article>
<article class="blog-card" style="left:800px">
  <div class="blog-img" style="background:linear-gradient(135deg,#d3b9c2,#8c5f74)" role="img" aria-label="Woman lifting dumbbells in a gym"></div>
  <span class="blog-date">14 - 03 - 2017</span>
  <div class="blog-body"><h4>Lorem ipsum dolor sit amet</h4><p>Adipiscing elit sed do eiu</p></div>
  <span class="blog-corner"></span>
</article>

<section class="testimonial">
  <span class="quote-mark">&ldquo;</span>
  <p class="quote-text">Lorem ipsum dolor sit amet, consectetur adipiscing elit, sed do eiusmod tempor incididunt ut labore et dolore magna aliqua. Ut enim ad minim veniam, quis nostrud exercitation ullamco laboris nisi ut aliquip ex ea commodo consequat. Duis aute irure dolor in reprehenderit in voluptate velit esse cillum dolore eu fugiat nulla pariatur. Excepteur sint occaecat cupidatat non proident, sunt in culpa qui officia deserunt mollit anim.</p>
  <span class="quote-name">MARLENE ASHBY</span>
  <div class="quote-dots"><span></span><span></span><span></span></div>
</section>

<footer class="site-footer">
  <div class="footer-brand"><div class="brand"><span class="brand-mark"></span>COREVIA</div></div>
  <div class="footer-col" style="left:320px"><h5>Navigation</h5><ul><li>Home</li><li>Team</li><li>Partners</li></ul></div>
  <div class="footer-col" style="left:500px"><h5>Quick Links</h5><ul><li>Blog</li><li>Store</li><li>Contact</li></ul></div>
  <div class="footer-col contact" style="left:680px"><h5>Contact Us</h5><ul><li>Marlow Bay, Kestrel Coast</li><li>0400 218 774</li><li>hello@corevia.com.au</li></ul></div>
  <div class="footer-col" style="left:900px"><h5>Stay Connected</h5>
    <div class="news"><span>Your email</span><b></b></div>
    <div class="follow">Follow us on <i></i><i></i><i></i></div>
  </div>
</footer>
<div class="copyright">© Copyright Corevia (aust) pty ltd. All Right Reserved</div>

</body>
</html>
```